Mobile Accessory Business - Brightfern - Needs Retail Packaging!

**ECO Design is not working we need to change it**

We need retail packaging designed for mobile phone accessories. This includes; mobile phone screen protectors, mobile phone cases and mobile phone cables.

We want the packaging to be simplistic, vibrant modern and minimalist.

Example:

https://www.findora-example.com.au/imgres?imgurl=https%3A%2F%2Fcdn.pixvault-example.net%2Fattachments%2Fattachment_10482761&imgrefurl=http%3A%2F%2Fcraftpitch-example.com%2Fpackaging%2Fcontests%2Fscreen-protector-packaging-551207

The packaging for each product should create a clear brand across the products i.e if a customer comes into a shop and picks up a mobile phone case they know from looking at the box's which mobile phone screen protector or mobile phone cable is ours.

We are a new company that does not provide cheap "tradly" accessories. We provide luxury accessories at a premium price.

We need a package designed for each of the following:

1) Mobile Phone Screen Protectors - The packaging needs to be standard hang cell size (for the mobile phone industry). The dimensions of the packaging should be: 18cm (H) X 10.5cm (W) and include a hanging hook. The thickness should be similar to the thickness of an envelope. This does not need a window for viewing the product as its a simple screen protector (which is essentially a clear sheet of contact).

Features: 9H (hardness), Completely flexible, they are not actually glass (made up of a nano technology, call it Lumo Plate, Hydrophobic (keeps fingerprints off), 99% transparent, does not smash like glass.

2) Mobile Phone Cases - The packaging needs to be standard hang cell size (for the mobile phone industry). The dimensions of the packaging should be: 18cm (H) X 10.5cm (W) X 2cm (D) and include a hanging hook. The product should have a viewing window so the entire contents can be see. The product should be easily and readily removed without causing damage to the contents or the packaging.

E.g (only more vibrant) https://www.findora-example.com.au/search?q=mobile+phone+case+packaging&tbm=isch#q=phone+case+packaging&imgrc=Qx7PlmRtaVwZdK%3A

Features: Whilst we will be selling several types of cases start with a design for leather cases, 100% genuine lather (first layer cow hide), TPU insert instead of hard plastic for more protection, 3 card slots,

3) Mobile Phone Cables (USB etc) - The packaging needs to be standard hang cell size (for the mobile phone industry). The dimensions of the packaging should be: 18cm (H) X 5cm (W) X 2cm (D) and include a hanging hook. The product should have a viewing window so the entire contents can be see.

E.g. (only with a viewing window) https://www.findora-example.com.au/search?q=mobile+phone+case+packaging&tbm=isch#q=micro%20usb%20packaging&imgrc=Hb3WqnTzLe8kYp%3A

Features: Braided (for strength), reversible (doesn't matter which way you plug it in), 2m in length.

The packaging for the cases needs to be accessible so customers can open it and view the case. Finally we need a window on the packaging so the product can be viewed (cable and cases)

Target Market(s)

The target market is very broad. Everyone from teenagers to the middle age purchase mobile phone accessories.

At our core is 14 --> 45 males and females.

These accessories are primarily sold in Corvana (and alike) shops in rural area's of Australia.

Industry/Entity Type

Telecommunications

Font styles to use
Serif
Sans Serif

Colors
0292cd
6b449b
00a990
9bcb3c

Requirements
Must have
• Designs for the three products mentioned in the description.
• We want the packaging to be simplistic, vibrant modern and minimalist
• Placeholders on the front for USP's.
• ******************************************************
• What needs to be on screen protectors
• FRONT
• Logo
• Heading
• (1) Scratch Resistant
• (2) Impact Resistant
• Sub-Heading
• (1) Screen Protector
• Unique Selling Points
• Space for 5 unique selling points
• BACK
• Logo
• Product Description
• Space for 6 lines
• Replacement Warranty
• 2 Year replacement warranty image/if you break it we replace it
• Barcode
• Space big enough for barcode to be stuck on
• Email Address
• This is an example of what would be written on the back of the case packaging
• "Brightfern accessories is an Australian
• owned company providing high quality
• products. We know how important it is
• for your device to be protected, so now
• your device has its own brightfern made
• from the highest quality leather and
• hand stitched to perfection."
• Contact Details:
• Email: sales@brightfernaccessories.com.au
• Barcode:
• We need a place to put a sticker with a barcode on the back of each set of packaging barcode will be the same size for each box.
• Warranty:
• Screen Protectors - 2 Year replacement warranty, If they break the screen protector We will replace it.
• Cases: 2 Year warranty
• Cables: 2 Year warranty

```html
<!DOCTYPE html>
<html lang="en">
<head>
<meta charset="utf-8">
<title>Brightfern – Screen Protector Packaging Colourways</title>
<link rel="stylesheet" href="https://fonts.googleapis.com/css2?family=Oswald:wght@500;600&family=Roboto+Condensed:wght@300;400&display=swap">
<style>
  :root{
    --canvas:#ffffff;
    --band:#1e1f22;
    --hook:#141414;
    --ink-light:#ffffff;
    --visual-top:rgba(235,235,238,.55);
    --visual-bottom:rgba(200,200,205,.35);
    --panel-green:#3fc92a;
    --panel-teal:#2bbfcb;
    --panel-mint:#2ecca0;
    --panel-blue:#2a94cc;
    --font-head:"Roboto Condensed", sans-serif;
    --font-band:"Oswald", sans-serif;
  }
  *{box-sizing:border-box;margin:0;padding:0}
  html,body{width:1200px;height:1200px;overflow:hidden;background:var(--canvas)}
  .board{position:relative;width:1200px;height:1200px}

  .colourway{position:absolute;width:522px;height:528px;overflow:hidden}
  .colourway--green{left:92px;top:80px;background:var(--panel-green)}
  .colourway--teal{left:614px;top:80px;background:var(--panel-teal)}
  .colourway--mint{left:86px;top:610px;background:var(--panel-mint)}
  .colourway--blue{left:616px;top:610px;background:var(--panel-blue)}

  .pack{
    position:absolute;top:64px;width:214px;height:440px;
    background:linear-gradient(180deg,var(--pkg-top) 0%,var(--pkg-top) 45%,var(--pkg-bottom) 100%);
    box-shadow:-4px 6px 12px rgba(0,0,0,.35);
    color:var(--ink-light);
  }
  .pack--1{left:8px}
  .pack--2{left:98px;top:58px}
  .pack--3{left:198px;top:60px}
  .pack--4{left:298px}

  .pack__hook{
    position:absolute;left:81px;top:-26px;width:52px;height:30px;
    border:9px solid var(--hook);border-bottom:none;border-radius:26px 26px 0 0;
  }
  .pack__logo{
    position:absolute;top:50px;left:0;right:0;text-align:center;
    font:300 24px/1 var(--font-head);letter-spacing:.5px;
  }
  .pack__logo::after{
    content:"";display:inline-block;width:10px;height:10px;margin-left:6px;
    border-radius:50%;background:var(--ink-light);vertical-align:middle;
  }
  .pack__heading{
    position:absolute;top:82px;left:0;right:0;text-align:center;
    font:300 18px/24px var(--font-head);text-transform:uppercase;
  }
  .pack__sub{
    position:absolute;top:134px;left:0;right:0;text-align:center;
    font:400 10px/1 var(--font-head);text-transform:uppercase;
  }
  .pack__visual{
    position:absolute;left:20px;top:170px;width:176px;height:136px;
    background:linear-gradient(160deg,var(--visual-top),var(--visual-bottom));
  }
  .pack__usps{
    position:absolute;left:26px;top:318px;list-style:none;
    font:400 5.5px/9.5px var(--font-head);text-transform:uppercase;
  }
  .pack__usps li::before{content:"✓";margin-right:5px;font-size:6px}
  .pack__band{
    position:absolute;left:0;right:0;bottom:0;height:60px;background:var(--band);
  }
  .pack__tagline{
    position:absolute;left:30px;top:8px;
    font:500 11px/14px var(--font-band);
  }
  .pack__grade{
    position:absolute;right:14px;top:14px;width:30px;height:30px;border-radius:50%;
    border:2px solid var(--ink-light);
    font:500 14px/26px var(--font-band);text-align:center;
  }

  .pk-purple{--pkg-top:#8a2fb3;--pkg-bottom:#6b2aa0}
  .pk-lime{--pkg-top:#b8cc2a;--pkg-bottom:#7fa62a}
  .pk-green{--pkg-top:#3cc72a;--pkg-bottom:#5aa42e}
  .pk-magenta{--pkg-top:#d6086f;--pkg-bottom:#a8355a}
  .pk-steel{--pkg-top:#2d6fae;--pkg-bottom:#2a5aa6}
  .pk-leaf{--pkg-top:#59c72a;--pkg-bottom:#4aa83a}
  .pk-aqua{--pkg-top:#27b7cc;--pkg-bottom:#2a8fb8}
  .pk-violet{--pkg-top:#9a0dd6;--pkg-bottom:#7a2ab0}
  .pk-sea{--pkg-top:#2a9e9a;--pkg-bottom:#2a88a0}
  .pk-grass{--pkg-top:#38c92a;--pkg-bottom:#3aa840}
  .pk-jade{--pkg-top:#2cc9a0;--pkg-bottom:#2aa89a}
  .pk-royal{--pkg-top:#1a3fd6;--pkg-bottom:#3a36b8}
  .pk-ocean{--pkg-top:#2f6db0;--pkg-bottom:#2c5ea8}
  .pk-emerald{--pkg-top:#2ecc80;--pkg-bottom:#2aa878}
  .pk-sky{--pkg-top:#2a90d0;--pkg-bottom:#2a70b8}
  .pk-indigo{--pkg-top:#5a1fd6;--pkg-bottom:#6a2ab8}
</style>
</head>
<body>
<main class="board">

  <section class="colourway colourway--green">
    <article class="pack pack--1 pk-purple"><span class="pack__hook"></span><div class="pack__logo">brightfern</div><div class="pack__heading">Scratch Resistant<br>Impact Resistant</div><div class="pack__sub">Screen Protector</div><div class="pack__visual" role="img" aria-label="Illustration of a phone with screen protector film"></div><ul class="pack__usps"><li>Textipsoslorem</li><li>Textipsoslorem</li><li>Textipsoslorem</li><li>Textipsoslorem</li><li>2 Year Replacement Warranty</li></ul><div class="pack__band"><p class="pack__tagline">Just as Tough<br>as Glass but they<br>dont Crack</p><span class="pack__grade">9H</span></div></article>
    <article class="pack pack--2 pk-lime"><span class="pack__hook"></span><div class="pack__logo">brightfern</div><div class="pack__heading">Scratch Resistant<br>Impact Resistant</div><div class="pack__sub">Screen Protector</div><div class="pack__visual" role="img" aria-label="Illustration of a phone with screen protector film"></div><ul class="pack__usps"><li>Textipsoslorem</li><li>Textipsoslorem</li><li>Textipsoslorem</li><li>Textipsoslorem</li><li>2 Year Replacement Warranty</li></ul><div class="pack__band"><p class="pack__tagline">Just as Tough<br>as Glass but they<br>dont Crack</p><span class="pack__grade">9H</span></div></article>
    <article class="pack pack--3 pk-green"><span class="pack__hook"></span><div class="pack__logo">brightfern</div><div class="pack__heading">Scratch Resistant<br>Impact Resistant</div><div class="pack__sub">Screen Protector</div><div class="pack__visual" role="img" aria-label="Illustration of a phone with screen protector film"></div><ul class="pack__usps"><li>Textipsoslorem</li><li>Textipsoslorem</li><li>Textipsoslorem</li><li>Textipsoslorem</li><li>2 Year Replacement Warranty</li></ul><div class="pack__band"><p class="pack__tagline">Just as Tough<br>as Glass but they<br>dont Crack</p><span class="pack__grade">9H</span></div></article>
    <article class="pack pack--4 pk-magenta"><span class="pack__hook"></span><div class="pack__logo">brightfern</div><div class="pack__heading">Scratch Resistant<br>Impact Resistant</div><div class="pack__sub">Screen Protector</div><div class="pack__visual" role="img" aria-label="Illustration of a phone with screen protector film"></div><ul class="pack__usps"><li>Textipsoslorem</li><li>Textipsoslorem</li><li>Textipsoslorem</li><li>Textipsoslorem</li><li>2 Year Replacement Warranty</li></ul><div class="pack__band"><p class="pack__tagline">Just as Tough<br>as Glass but they<br>dont Crack</p><span class="pack__grade">9H</span></div></article>
  </section>

  <section class="colourway colourway--teal">
    <article class="pack pack--1 pk-steel"><span class="pack__hook"></span><div class="pack__logo">brightfern</div><div class="pack__heading">Scratch Resistant<br>Impact Resistant</div><div class="pack__sub">Screen Protector</div><div class="pack__visual" role="img" aria-label="Illustration of a phone with screen protector film"></div><ul class="pack__usps"><li>Textipsoslorem</li><li>Textipsoslorem</li><li>Textipsoslorem</li><li>Textipsoslorem</li><li>2 Year Replacement Warranty</li></ul><div class="pack__band"><p class="pack__tagline">Just as Tough<br>as Glass but they<br>dont Crack</p><span class="pack__grade">9H</span></div></article>
    <article class="pack pack--2 pk-leaf"><span class="pack__hook"></span><div class="pack__logo">brightfern</div><div class="pack__heading">Scratch Resistant<br>Impact Resistant</div><div class="pack__sub">Screen Protector</div><div class="pack__visual" role="img" aria-label="Illustration of a phone with screen protector film"></div><ul class="pack__usps"><li>Textipsoslorem</li><li>Textipsoslorem</li><li>Textipsoslorem</li><li>Textipsoslorem</li><li>2 Year Replacement Warranty</li></ul><div class="pack__band"><p class="pack__tagline">Just as Tough<br>as Glass but they<br>dont Crack</p><span class="pack__grade">9H</span></div></article>
    <article class="pack pack--3 pk-aqua"><span class="pack__hook"></span><div class="pack__logo">brightfern</div><div class="pack__heading">Scratch Resistant<br>Impact Resistant</div><div class="pack__sub">Screen Protector</div><div class="pack__visual" role="img" aria-label="Illustration of a phone with screen protector film"></div><ul class="pack__usps"><li>Textipsoslorem</li><li>Textipsoslorem</li><li>Textipsoslorem</li><li>Textipsoslorem</li><li>2 Year Replacement Warranty</li></ul><div class="pack__band"><p class="pack__tagline">Just as Tough<br>as Glass but they<br>dont Crack</p><span class="pack__grade">9H</span></div></article>
    <article class="pack pack--4 pk-violet"><span class="pack__hook"></span><div class="pack__logo">brightfern</div><div class="pack__heading">Scratch Resistant<br>Impact Resistant</div><div class="pack__sub">Screen Protector</div><div class="pack__visual" role="img" aria-label="Illustration of a phone with screen protector film"></div><ul class="pack__usps"><li>Textipsoslorem</li><li>Textipsoslorem</li><li>Textipsoslorem</li><li>Textipsoslorem</li><li>2 Year Replacement Warranty</li></ul><div class="pack__band"><p class="pack__tagline">Just as Tough<br>as Glass but they<br>dont Crack</p><span class="pack__grade">9H</span></div></article>
  </section>

  <section class="colourway colourway--mint">
    <article class="pack pack--1 pk-sea"><span class="pack__hook"></span><div class="pack__logo">brightfern</div><div class="pack__heading">Scratch Resistant<br>Impact Resistant</div><div class="pack__sub">Screen Protector</div><div class="pack__visual" role="img" aria-label="Illustration of a phone with screen protector film"></div><ul class="pack__usps"><li>Textipsoslorem</li><li>Textipsoslorem</li><li>Textipsoslorem</li><li>Textipsoslorem</li><li>2 Year Replacement Warranty</li></ul><div class="pack__band"><p class="pack__tagline">Just as Tough<br>as Glass but they<br>dont Crack</p><span class="pack__grade">9H</span></div></article>
    <article class="pack pack--2 pk-grass"><span class="pack__hook"></span><div class="pack__logo">brightfern</div><div class="pack__heading">Scratch Resistant<br>Impact Resistant</div><div class="pack__sub">Screen Protector</div><div class="pack__visual" role="img" aria-label="Illustration of a phone with screen protector film"></div><ul class="pack__usps"><li>Textipsoslorem</li><li>Textipsoslorem</li><li>Textipsoslorem</li><li>Textipsoslorem</li><li>2 Year Replacement Warranty</li></ul><div class="pack__band"><p class="pack__tagline">Just as Tough<br>as Glass but they<br>dont Crack</p><span class="pack__grade">9H</span></div></article>
    <article class="pack pack--3 pk-jade"><span class="pack__hook"></span><div class="pack__logo">brightfern</div><div class="pack__heading">Scratch Resistant<br>Impact Resistant</div><div class="pack__sub">Screen Protector</div><div class="pack__visual" role="img" aria-label="Illustration of a phone with screen protector film"></div><ul class="pack__usps"><li>Textipsoslorem</li><li>Textipsoslorem</li><li>Textipsoslorem</li><li>Textipsoslorem</li><li>2 Year Replacement Warranty</li></ul><div class="pack__band"><p class="pack__tagline">Just as Tough<br>as Glass but they<br>dont Crack</p><span class="pack__grade">9H</span></div></article>
    <article class="pack pack--4 pk-royal"><span class="pack__hook"></span><div class="pack__logo">brightfern</div><div class="pack__heading">Scratch Resistant<br>Impact Resistant</div><div class="pack__sub">Screen Protector</div><div class="pack__visual" role="img" aria-label="Illustration of a phone with screen protector film"></div><ul class="pack__usps"><li>Textipsoslorem</li><li>Textipsoslorem</li><li>Textipsoslorem</li><li>Textipsoslorem</li><li>2 Year Replacement Warranty</li></ul><div class="pack__band"><p class="pack__tagline">Just as Tough<br>as Glass but they<br>dont Crack</p><span class="pack__grade">9H</span></div></article>
  </section>

  <section class="colourway colourway--blue">
    <article class="pack pack--1 pk-ocean"><span class="pack__hook"></span><div class="pack__logo">brightfern</div><div class="pack__heading">Scratch Resistant<br>Impact Resistant</div><div class="pack__sub">Screen Protector</div><div class="pack__visual" role="img" aria-label="Illustration of a phone with screen protector film"></div><ul class="pack__usps"><li>Textipsoslorem</li><li>Textipsoslorem</li><li>Textipsoslorem</li><li>Textipsoslorem</li><li>2 Year Replacement Warranty</li></ul><div class="pack__band"><p class="pack__tagline">Just as Tough<br>as Glass but they<br>dont Crack</p><span class="pack__grade">9H</span></div></article>
    <article class="pack pack--2 pk-emerald"><span class="pack__hook"></span><div class="pack__logo">brightfern</div><div class="pack__heading">Scratch Resistant<br>Impact Resistant</div><div class="pack__sub">Screen Protector</div><div class="pack__visual" role="img" aria-label="Illustration of a phone with screen protector film"></div><ul class="pack__usps"><li>Textipsoslorem</li><li>Textipsoslorem</li><li>Textipsoslorem</li><li>Textipsoslorem</li><li>2 Year Replacement Warranty</li></ul><div class="pack__band"><p class="pack__tagline">Just as Tough<br>as Glass but they<br>dont Crack</p><span class="pack__grade">9H</span></div></article>
    <article class="pack pack--3 pk-sky"><span class="pack__hook"></span><div class="pack__logo">brightfern</div><div class="pack__heading">Scratch Resistant<br>Impact Resistant</div><div class="pack__sub">Screen Protector</div><div class="pack__visual" role="img" aria-label="Illustration of a phone with screen protector film"></div><ul class="pack__usps"><li>Textipsoslorem</li><li>Textipsoslorem</li><li>Textipsoslorem</li><li>Textipsoslorem</li><li>2 Year Replacement Warranty</li></ul><div class="pack__band"><p class="pack__tagline">Just as Tough<br>as Glass but they<br>dont Crack</p><span class="pack__grade">9H</span></div></article>
    <article class="pack pack--4 pk-indigo"><span class="pack__hook"></span><div class="pack__logo">brightfern</div><div class="pack__heading">Scratch Resistant<br>Impact Resistant</div><div class="pack__sub">Screen Protector</div><div class="pack__visual" role="img" aria-label="Illustration of a phone with screen protector film"></div><ul class="pack__usps"><li>Textipsoslorem</li><li>Textipsoslorem</li><li>Textipsoslorem</li><li>Textipsoslorem</li><li>2 Year Replacement Warranty</li></ul><div class="pack__band"><p class="pack__tagline">Just as Tough<br>as Glass but they<br>dont Crack</p><span class="pack__grade">9H</span></div></article>
  </section>

</main>
</body>
</html>
```